Einladungskarten Design
Zielgruppe
Die Zielgruppe besteht aus allen Privatpersonen, die eine Feier planen und auf der Suche nach individuellen, professionell gestalteten Einladungskarten für Ihre Feier sind:
Hochzeit
Geburtstag (meistens runde Geburtstage)
Mottoparty´s
Danksagung zur Gebur
Aufgabenstellung
Für das Online-Angebot www.kartenfreude-atelier.de werden kreative Vorschläge für Einladungskarten und Danksagungskarten in verschiedenen Kategorien gesucht: Hochzeit, Geburtstag, Party, Mottoparty, Geburt und weitere Themen. Das Thema ist wählbar, da für alle Kategorien neue, frische Entwürfe benötigt werden.
Dies ist kein Wettbewerb im herkömmlichen Sinne, da es keinen einzelnen Gewinner gibt. Jeder Kartenentwurf, der für das Online Angebot ausgewählt wird, wird mit 100,00 Eur honoriert.
Voraussetzung für die Honorarzahlung ist das Einverständnis der Veröffentlichung und die Übertragung der Nutzungsrechte.

```html
<!DOCTYPE html>
<html lang="de">
<head>
<meta charset="utf-8">
<title>Einladung – 40. Geburtstag</title>
<link href="https://fonts.googleapis.com/css2?family=Crimson+Text:wght@400;600&display=swap" rel="stylesheet">
<style>
  :root {
    --page: #ffffff;
    --card: #ffffff;
    --card-edge: #d9d9d9;
    --fold: #cfcfcf;
    --band: #981a55;
    --band-text: #f6e6ee;
    --accent-text: #c4457f;
    --ghost: rgba(235, 200, 220, 0.75);
    --orchid-light: #d98fd6;
    --orchid-mid: #b765c0;
    --orchid-deep: #8a1f9a;
  }
  * { margin: 0; padding: 0; box-sizing: border-box; }
  html, body {
    width: 1200px; height: 1200px; overflow: hidden;
    background: var(--page);
    font-family: "Crimson Text", "Times New Roman", serif;
  }
  .canvas { position: relative; width: 1200px; height: 1200px; }

  .card {
    position: absolute; left: 45px; width: 1110px; height: 345px;
    background: var(--card);
    border: 1px solid var(--card-edge);
    box-shadow: 0 1px 3px rgba(0,0,0,0.12);
    overflow: hidden;
  }
  .card--outside { top: 180px; }
  .card--inside { top: 687px; }

  .fold {
    position: absolute; left: 554px; top: 0; width: 1px; height: 100%;
    background: var(--fold);
  }

  .band {
    position: absolute; left: 0; width: 100%; height: 46px;
    background: var(--band);
  }
  .card--outside .band { top: 234px; }
  .card--inside .band { top: 234px; height: 46px; }

  .orchid-corner {
    position: absolute; left: 0; top: 142px; width: 292px; height: 203px;
    background: radial-gradient(ellipse at 45% 65%, var(--orchid-deep) 0%, var(--orchid-mid) 35%, var(--orchid-light) 70%, rgba(217,143,214,0) 100%);
    border-radius: 48% 52% 0 0 / 60% 60% 0 0;
  }
  .card .band.over-flower { opacity: 0.88; }

  .orchid-branch {
    position: absolute; left: 555px; top: 25px; width: 240px; height: 297px;
    background: radial-gradient(ellipse at 45% 30%, var(--orchid-mid) 0%, var(--orchid-light) 40%, rgba(217,143,214,0.55) 62%, rgba(217,143,214,0) 78%);
    border-radius: 40%;
  }

  .title-echo {
    position: absolute; left: 842px; top: 212px;
    font-size: 40px; line-height: 40px; letter-spacing: 1px;
    color: var(--ghost);
    transform: scaleY(-1);
    white-space: nowrap;
  }
  .title {
    position: absolute; left: 637px; top: 228px;
    font-size: 66px; line-height: 52px; letter-spacing: 7px;
    color: #ffffff; font-weight: 400;
    white-space: nowrap;
  }

  .message {
    position: absolute; left: 582px; top: 240px;
    color: var(--band-text); font-size: 13.5px; line-height: 15px;
    letter-spacing: 0.2px; white-space: nowrap;
  }
  .message .age { font-size: 24px; line-height: 15px; color: #ffffff; }
  .note {
    position: absolute; left: 582px; top: 295px;
    color: var(--accent-text); font-size: 13.5px; letter-spacing: 0.2px;
    white-space: nowrap;
  }
</style>
</head>
<body>
<div class="canvas">

  <section class="card card--outside">
    <div class="orchid-corner" role="img" aria-label="Foto einer rosa Orchideenblüte, angeschnitten in der Ecke"></div>
    <div class="band over-flower"></div>
    <div class="fold"></div>
    <div class="orchid-branch" role="img" aria-label="Foto eines Orchideenzweigs mit Blüte und Knospen"></div>
    <div class="title-echo" aria-hidden="true">EINLADUNG</div>
    <h1 class="title">EINLADUNG</h1>
  </section>

  <section class="card card--inside">
    <div class="orchid-corner" role="img" aria-label="Foto einer rosa Orchideenblüte, angeschnitten in der Ecke"></div>
    <div class="band over-flower"></div>
    <p class="message">
      Ich lade Euch recht herzlich zu meinem <span class="age">40. Geburtstag</span> ein.<br>
      Am 01.01.2008, um 20.00 Uhr findet die große Party in unserem Garten statt.
    </p>
    <p class="note">Wer nicht kommen kann, gibt mir kurz unter der Rufnummer 09876/543210 Bescheid</p>
  </section>

</div>
</body>
</html>
```